Carton Box Packaging For Motorcycle Brake Shoe - Varonel Brand

Packaging Dimensions: 125mm (H) x 125mm (W) x 31mm (D)
We would like to design a genuine Carton box Packaging for motorcycle Brake Shoe.
This is a critical part of the motorcycle, so we need the packaging to reflect elegant impression.
Varonel, is one of the leading companies for manufacturing Motorcycles, located in Egypt. Our company is offering high-quality products, the best in the local market, with very competitive prices.
We have a limited time to get this project done, So we Highly appreciate receiving your designs ASAP.
Target Market(s)
Economical Motorcycle Buyers
Colors
Designer to choose colors to be used in the design.
Look and feel

```html
<!DOCTYPE html>
<html lang="en">
<head>
<meta charset="utf-8">
<title>Varonel Motorcycle Brake Shoe – Carton Artwork</title>
<link rel="stylesheet" href="https://fonts.googleapis.com/css2?family=Exo+2:ital,wght@1,900&family=Barlow+Semi+Condensed:wght@500&display=swap">
<style>
  :root {
    --page: #ffffff;
    --brand-red: #d2232b;
    --panel-blue: #26367e;
    --panel-blue-deep: #1f2a6b;
    --glow-teal: #2f7d8f;
    --ink-white: #ffffff;
    --steel-light: #b3ada2;
    --steel-mid: #8a8477;
    --steel-dark: #3f3b35;
    --seal-gold: #d8b13e;
    --seal-gold-light: #f3d36a;
    --seal-gold-dark: #8a6a17;
    --seal-rim: #2a2410;
  }
  * { box-sizing: border-box; margin: 0; padding: 0; }
  html, body { width: 1200px; height: 679px; overflow: hidden; background: var(--page); }
  .canvas { position: relative; width: 1200px; height: 679px; }

  .carton-face {
    position: absolute;
    top: 143px;
    width: 472px;
    height: 378px;
    display: flex;
  }
  .carton-face--first { left: 127px; }
  .carton-face--second { left: 599px; }

  .side-band {
    position: relative;
    width: 94px;
    height: 100%;
    background: var(--brand-red);
  }
  .side-title {
    position: absolute;
    left: 50%;
    top: 172px;
    transform: translate(-50%, -50%) rotate(-90deg);
    font-family: "Exo 2", sans-serif;
    font-style: italic;
    font-weight: 900;
    font-size: 27px;
    line-height: 27px;
    color: var(--ink-white);
    text-align: center;
    white-space: nowrap;
    letter-spacing: 0.6px;
  }
  .side-brand {
    position: absolute;
    left: 50%;
    top: 302px;
    transform: translate(-50%, -50%) rotate(-90deg);
    display: flex;
    align-items: center;
    gap: 5px;
    font-family: "Exo 2", sans-serif;
    font-style: italic;
    font-weight: 900;
    font-size: 13px;
    color: var(--ink-white);
    white-space: nowrap;
  }

  .front-panel {
    position: relative;
    flex: 1;
    height: 100%;
    overflow: hidden;
    background:
      radial-gradient(circle at 50% 58%, var(--glow-teal) 0%, rgba(47,125,143,0.45) 28%, rgba(37,51,122,0) 55%),
      linear-gradient(160deg, var(--panel-blue) 0%, var(--panel-blue-deep) 100%);
  }
  .brand-mark {
    position: absolute;
    top: 30px;
    left: 0;
    right: 0;
    display: flex;
    justify-content: center;
    align-items: center;
    gap: 5px;
    font-family: "Exo 2", sans-serif;
    font-style: italic;
    font-weight: 900;
    font-size: 15px;
    color: var(--ink-white);
  }
  .brand-dot {
    width: 12px; height: 12px;
    border-radius: 50%;
    background: var(--ink-white);
    flex: none;
  }
  .side-brand .brand-dot { width: 10px; height: 10px; }

  .product-title {
    position: absolute;
    top: 82px;
    left: 0;
    right: 0;
    text-align: center;
    font-family: "Exo 2", sans-serif;
    font-style: italic;
    font-weight: 900;
    font-size: 26px;
    line-height: 23px;
    color: var(--ink-white);
    letter-spacing: 0.3px;
  }
  .product-photo {
    position: absolute;
    left: 81px;
    top: 134px;
    width: 202px;
    height: 199px;
    border-radius: 50%;
    background: radial-gradient(ellipse at 50% 50%,
      rgba(47,125,143,0) 0%,
      rgba(47,125,143,0) 46%,
      var(--steel-mid) 52%,
      var(--steel-light) 62%,
      var(--steel-mid) 78%,
      var(--steel-dark) 100%);
  }
  .quality-seal {
    position: absolute;
    left: 246px;
    top: 197px;
    width: 59px;
    height: 59px;
    border-radius: 50%;
    background: radial-gradient(circle at 40% 35%, var(--seal-gold-light) 0%, var(--seal-gold) 55%, var(--seal-gold-dark) 100%);
    border: 2px solid var(--seal-rim);
  }
  .tagline {
    position: absolute;
    top: 344px;
    left: 0;
    right: 18px;
    text-align: center;
    font-family: "Barlow Semi Condensed", sans-serif;
    font-weight: 500;
    font-size: 10px;
    color: var(--ink-white);
  }
</style>
</head>
<body>
<div class="canvas">
  <section class="carton-face carton-face--first">
    <div class="side-band">
      <div class="side-title">MOTORCYCLE<br>BRAKE SHOE</div>
      <div class="side-brand"><span class="brand-dot"></span>Varonel</div>
    </div>
    <div class="front-panel">
      <div class="brand-mark"><span class="brand-dot"></span>Varonel</div>
      <h1 class="product-title">MOTORCYCLE<br>BRAKE SHOE</h1>
      <div class="product-photo" role="img" aria-label="Photo of a pair of motorcycle drum brake shoes joined by two springs"></div>
      <div class="quality-seal" role="img" aria-label="Gold genuine-parts seal"></div>
      <p class="tagline">High-Quality and Competitive Prices</p>
    </div>
  </section>

  <section class="carton-face carton-face--second">
    <div class="side-band">
      <div class="side-title">MOTORCYCLE<br>BRAKE SHOE</div>
      <div class="side-brand"><span class="brand-dot"></span>Varonel</div>
    </div>
    <div class="front-panel">
      <div class="brand-mark"><span class="brand-dot"></span>Varonel</div>
      <h2 class="product-title">MOTORCYCLE<br>BRAKE SHOE</h2>
      <div class="product-photo" role="img" aria-label="Photo of a pair of motorcycle drum brake shoes joined by two springs"></div>
      <div class="quality-seal" role="img" aria-label="Gold genuine-parts seal"></div>
      <p class="tagline">High-Quality and Competitive Prices</p>
    </div>
  </section>
</div>
</body>
</html>
```